Melvari Piano Studio Creative Card (EXISTING LOGO)

Hi all
We need an artistic, creative and modern business card design for our piano studio. Logo is attached, please let us know if you need other file formats.
The business card should convey high-end, prestigiousness, and be minimalist in feel. It should not look corporate or childish.
Rounded corners or creative shapes only, no regular square corners. Card should be double-sided. Can be portrait or landscape oriented. No preference to size either. Standard or custom size both okay.
We will not be giving out thousands of cards due to the nature of our business. We want to make sure that each business card we hand out, people will appreciate the design and printing quality that took place.
Please note, as the logo is supplied, we need more than just a layout with name and phone number etc inserted. Quite frankly,we can do that ourselves. We are interested in designs that has the different special printing methods in mind during the designing process. We are particularly interested in the effects of:
- Spot UV Varnish
- Foil
- Thermography
- Letterpress
- Die Cut
- Lamination
Colours does not have to be limited to black and white.
Information to be included:
Name (with qualification attached)
Mobile
website "melvari.com.au"
Designs submitted should include description of the printing method. The final format should be ready to be sent to printer with detailed printing method and colour (if applicable) instructions.
Much thanks in advance.
Updates
as per request from a designer, eps format file uploaded.

```html
<!DOCTYPE html>
<html lang="en">
<head>
<meta charset="utf-8">
<title>Melvari Piano Studio – Business Card</title>
<link rel="stylesheet" href="https://fonts.googleapis.com/css2?family=Michroma&family=Questrial&display=swap">
<style>
  :root {
    --backdrop: #d8d2ca;
    --card-white: #ffffff;
    --card-black-top: #1c1c1c;
    --card-black-bottom: #050505;
    --ink-dark: #111111;
    --ink-light: #ffffff;
    --ink-soft: #d9d9d9;
    --rule: #6b6b6b;
  }
  * { box-sizing: border-box; margin: 0; padding: 0; }
  html, body {
    width: 1200px;
    height: 534px;
    overflow: hidden;
    background: var(--backdrop);
  }
  .stage {
    position: relative;
    width: 1200px;
    height: 534px;
  }
  .card {
    position: absolute;
    top: 68px;
    width: 227px;
    height: 398px;
    border-radius: 58px 58px 2px 2px;
    overflow: hidden;
    display: flex;
    flex-direction: column;
  }
  .card--front { left: 348px; }
  .card--back  { left: 624px; }

  .card__face {
    height: 225px;
    background: var(--card-white);
    display: flex;
    flex-direction: column;
    align-items: center;
    justify-content: center;
    gap: 18px;
    padding-top: 10px;
  }
  .mark__square {
    width: 34px;
    height: 34px;
    background: var(--ink-dark);
  }
  .mark__name {
    font-family: "Michroma", sans-serif;
    font-weight: 400;
    font-size: 24px;
    letter-spacing: 3px;
    margin-right: -3px;
    line-height: 1;
    color: var(--ink-dark);
  }

  .card__panel {
    flex: 1;
    background: linear-gradient(180deg, var(--card-black-top), var(--card-black-bottom));
    color: var(--ink-light);
    text-align: center;
  }
  .brand {
    padding-top: 62px;
    font-family: "Michroma", sans-serif;
    font-weight: 400;
  }
  .brand__name {
    display: block;
    font-size: 25px;
    letter-spacing: 4px;
    margin-right: -4px;
    line-height: 1;
  }
  .brand__tag {
    display: block;
    margin-top: 12px;
    font-size: 11px;
    letter-spacing: 5px;
    margin-right: -5px;
    line-height: 1;
  }
  .contact {
    padding-top: 40px;
    font-family: "Questrial", sans-serif;
  }
  .contact__name {
    font-size: 18px;
    letter-spacing: 0.6px;
    line-height: 1;
    font-weight: 400;
  }
  .contact__role {
    margin-top: 4px;
    font-size: 9px;
    letter-spacing: 0.4px;
    color: var(--ink-soft);
  }
  .contact__rule {
    width: 154px;
    height: 1px;
    margin: 16px auto 16px;
    background: var(--rule);
    border: 0;
  }
  .contact__line {
    font-size: 13.5px;
    letter-spacing: 0.6px;
    line-height: 18px;
  }
</style>
</head>
<body>
  <main class="stage">
    <section class="card card--front" aria-label="Card front">
      <div class="card__face mark">
        <span class="mark__square"></span>
        <span class="mark__name">MELVARI</span>
      </div>
      <div class="card__panel">
        <h1 class="brand">
          <span class="brand__name">MELVARI</span>
          <span class="brand__tag">PIANO STUDIO</span>
        </h1>
      </div>
    </section>

    <section class="card card--back" aria-label="Card back">
      <div class="card__face mark">
        <span class="mark__square"></span>
        <span class="mark__name">MELVARI</span>
      </div>
      <div class="card__panel">
        <div class="contact">
          <p class="contact__name">ADRIAN KELL</p>
          <p class="contact__role">FOUNDER, CEO</p>
          <hr class="contact__rule">
          <p class="contact__line">000.000.0000</p>
          <p class="contact__line">WWW.MELVARI.COM.AU</p>
        </div>
      </div>
    </section>
  </main>
</body>
</html>
```